BHA Brochure

A Brochure based on my website
www.brighthollowalliance.org that was made on sketch bazaar

Project Deadline Extended
Reason: Due to the Holiday here in the states and to give the new designers a little more time I would like to extend the date. I will also be out of town for a few days. Thank you.

```html
<!DOCTYPE html>
<html lang="en">
<head>
<meta charset="utf-8">
<title>Bright Hollow Alliance Brochure</title>
<link href="https://fonts.googleapis.com/css2?family=PT+Sans+Narrow:wght@400;700&family=Open+Sans:wght@400;700&display=swap" rel="stylesheet">
<style>
  :root {
    --navy: #1f4d8c;
    --blue: #1c4a93;
    --deep-blue: #123a78;
    --red: #a01f26;
    --dark-red: #8a1820;
    --plum: #7a0f3a;
    --grey-text: #6d6e71;
    --ink: #333333;
    --bg-top: #eef0f2;
    --bg-bottom: #d9dbde;
    --panel: #f4f5f6;
    --white: #ffffff;
  }
  * { margin: 0; padding: 0; box-sizing: border-box; }
  html, body { width: 1200px; height: 927px; overflow: hidden; }
  body { font-family: "Open Sans", Arial, sans-serif; }
  .brochure {
    position: relative; width: 1200px; height: 927px; overflow: hidden;
    background: linear-gradient(180deg, var(--bg-top), var(--bg-bottom));
  }
  .shapes { position: absolute; inset: 0; }
  .join-title {
    position: absolute; left: 62px; top: 38px;
    font-family: "PT Sans Narrow", sans-serif; font-weight: 400;
    font-size: 36px; color: var(--navy); letter-spacing: -0.3px;
  }
  .step {
    position: absolute; left: 42px; width: 343px;
    background: linear-gradient(90deg, var(--panel), #e4e6e8);
    border-radius: 14px 0 14px 14px;
  }
  .step-1 { top: 84px; height: 120px; }
  .step-2 { top: 232px; height: 118px; }
  .step-3 { top: 378px; height: 118px; }
  .step-num {
    position: absolute; left: -22px; top: 28px; width: 56px; height: 56px;
    border-radius: 50%; background: var(--white);
    box-shadow: 0 1px 4px rgba(0,0,0,.25);
    font-family: "PT Sans Narrow", sans-serif; font-weight: 700;
    font-size: 46px; line-height: 56px; text-align: center; color: var(--navy);
  }
  .step-body { position: absolute; left: 44px; top: 10px; right: 20px; }
  .step h3 {
    font-family: "PT Sans Narrow", sans-serif; font-weight: 400;
    font-size: 21px; color: #444; margin-bottom: 4px;
  }
  .step h3 .link { color: var(--navy); }
  .step p { font-size: 10.8px; line-height: 18px; color: var(--grey-text); }
  .step .accent { color: var(--plum); }
  .guidelines {
    position: absolute; left: 416px; top: 42px; width: 369px; height: 476px;
    background: linear-gradient(180deg, #f7f8f9, #e9ebee);
    border: 1px solid #8eaacb; padding: 16px 8px 0 6px;
    font-size: 13px; line-height: 18px; color: var(--ink);
  }
  .guidelines-title {
    float: right; margin: -6px 2px 2px 8px; width: 136px;
    font-family: "PT Sans Narrow", sans-serif; color: var(--navy);
    line-height: 1; font-weight: 400;
  }
  .guidelines-title .small { display: block; font-size: 22px; }
  .guidelines-title .big { display: block; font-size: 40px; margin-left: -2px; }
  .guidelines ol { padding-left: 20px; }
  .guidelines h4 { font-size: 13px; margin-top: 14px; }
  .guidelines .policy { padding-left: 8px; }
  .network-text {
    position: absolute; left: 416px; top: 562px; width: 360px;
    font-size: 17.5px; line-height: 22px; color: var(--white);
  }
  .brand {
    position: absolute; left: 822px; top: 572px; width: 300px; text-align: center;
    font-family: "PT Sans Narrow", sans-serif; color: var(--white);
    font-size: 44px; line-height: 44px;
  }
  .brand-tag {
    position: absolute; left: 830px; top: 694px; width: 262px; text-align: center;
    font-size: 11.5px; line-height: 14px; color: #f3dede;
  }
  .footer-name {
    position: absolute; left: 34px; top: 796px;
    font-family: "PT Sans Narrow", sans-serif; font-size: 26px; color: var(--navy);
  }
  .footer-role {
    position: absolute; left: 34px; top: 824px;
    font-family: "PT Sans Narrow", sans-serif; font-size: 18px; color: #555;
  }
  .contact {
    position: absolute; left: 416px; top: 808px; font-style: normal;
    font-size: 12px; line-height: 15px; color: #444;
  }
  .url-tab {
    position: absolute; left: 970px; top: 840px;
    font-size: 12.5px; color: var(--white);
  }
</style>
</head>
<body>
<div class="brochure">
  <svg class="shapes" width="1200" height="927" viewBox="0 0 1200 927">
    <defs>
      <linearGradient id="team-tone" x1="0" y1="0" x2="1" y2="1">
        <stop offset="0" stop-color="#d9dde2"/>
        <stop offset="1" stop-color="#8a8f99"/>
      </linearGradient>
      <linearGradient id="office-tone" x1="0" y1="0" x2="1" y2="1">
        <stop offset="0" stop-color="#c9d3dc"/>
        <stop offset="1" stop-color="#a58f7c"/>
      </linearGradient>
      <linearGradient id="column-blue" x1="0" y1="0" x2="1" y2="1">
        <stop offset="0" stop-color="#2457a3"/>
        <stop offset="1" stop-color="#0f336c"/>
      </linearGradient>
    </defs>
    <polygon points="817,420 960,80 1200,80 1200,927 817,927" fill="url(#column-blue)"/>
    <polygon points="850,485 872,430 1200,430 1200,485" fill="var(--red)"/>
    <polygon points="828,430 967,84 1200,84 1200,426" fill="#ffffff"/>
    <polygon points="835,424 971,90 1200,90 1200,420" fill="url(#office-tone)" role="img" aria-label="Photo of two smiling professionals working at a laptop in a bright office"/>
    <polygon points="0,527 1170,527 1092,760 0,760" fill="var(--red)"/>
    <rect x="5" y="542" width="346" height="204" fill="#ffffff"/>
    <polygon points="351,574 394,598 351,622" fill="#ffffff"/>
    <rect x="8" y="545" width="340" height="198" fill="url(#team-tone)" role="img" aria-label="Photo of a team of four business professionals standing together"/>
    <rect x="703" y="787" width="76" height="76" fill="#ffffff" stroke="#b4b6b9"/>
    <rect x="706" y="790" width="70" height="70" fill="#9c8572" role="img" aria-label="Portrait photo of the moderator"/>
    <polygon points="820,838 935,838 925,870 815,870" fill="var(--dark-red)"/>
    <polygon points="940,832 1200,832 1200,870 930,870" fill="var(--red)"/>
  </svg>

  <h1 class="join-title">Join the Listserv. It's Easy!</h1>

  <section class="step step-1">
    <div class="step-num">1</div>
    <div class="step-body">
      <h3>Visit <span class="link">brighthollowalliance.org</span>.</h3>
      <p>Click on the "Contact Us" tab, fill out the form and let us know that you'd like to become a member. You will then be sent an invitation to join from <span class="accent">Listmail Groups</span>.</p>
    </div>
  </section>
  <section class="step step-2">
    <div class="step-num">2</div>
    <div class="step-body">
      <h3>Follow the Prompts</h3>
      <p>Next, follow the prompts to "Join this Mailing List,. There will be two prompts for that. You do not need to select the option to "Join the Group," <span class="accent">only JOIN THIS MAILING LIST</span>.</p>
    </div>
  </section>
  <section class="step step-3">
    <div class="step-num">3</div>
    <div class="step-body">
      <h3>You're In!</h3>
      <p>Once you join the mailing list, you will receive an email welcoming you to the listserv and telling you how to use this wonderful resource.</p>
    </div>
  </section>

  <section class="guidelines">
    <h2 class="guidelines-title"><span class="small">Forum</span><span class="big">Guidlines</span></h2>
    <ol>
      <li><b>DO NOT USE REPLY ALL</b>. Please make sure that if you are replying to an email on the listserv, ensure that you reply ONLY to the person sending the email and NOT to the entire listserv.</li>
      <li><b>ALWAYS FILL IN THE SUBJECT LINE.</b> This helps people to decide if they want to open the posting.</li>
      <li>Do not include your comments as an attachment.</li>
      <li>Always sign your name (first and last).</li>
      <li>When writing about a particular case, <b>avoid details that could possibly identify the person</b>.</li>
      <li>Postings should NEVER include judgmental comments about any individual or facility. All such commentary should be done offline.</li>
    </ol>
    <h4>Advertising Policy.</h4>
    <p class="policy"><b>a.</b> Any member may post notices about services for clients or professionals, but should be judicious, as this is not an advertising forum. If someone is looking for a program for a client, facility representatives should reply only to the person who made the inquiry.</p>
    <p class="policy"><b>b.</b> Members looking for jobs, office space, etc., may post queries. Responses, however, should be made only to the sender and not to the entire listserv.</p>
  </section>

  <p class="network-text">The BRIGHT HOLLOW ALLIANCE is a network of more than 500 professionals working together to help those suffering with mental health, substance abuse and addiction issues. Join our online conversation and meet us for lunch on First Fridays at the Harbor Table.</p>

  <div class="brand">Bright Hollow<br>Alliance</div>
  <p class="brand-tag">A collaboration of mental health, substance abuse and addiction professionals</p>

  <div class="footer-name">Bright Hollow Alliance</div>
  <div class="footer-role">Dana Whitfield, LICSW, CASAC, Moderator</div>
  <address class="contact">2240 Linden Ave., NW, Washington, DC 20008<br>202-555-0148<br>www.brighthollowalliance.org</address>
  <div class="url-tab">brighthollowalliance.org</div>
</div>
</body>
</html>
```